Welding and farication business card

Business name Tbm Welding & Fabrication

I need a business card made for my welding and fabrication business that is bold and stands out. My business is both welding repairs on machinery and anything else you can imagine as well as fabricating new products. i have used this service before and was very happy with the out come of my design logo. i think the card should remain fairly simple and classy but also be bold. I think a black card would best be suited to the talk with my logo on it. i feel the back of the card should just have my logo and the front have my logo email, website and phone number and maybe incorporate a facebook and instagram simple if it can be made look good these arnt a necessity.
I have included both my logo and some business card ideas below

Target Market(s)

Farmers, heavy industry, earthmoving, trucking

Industry/Entity Type

Engineering

Contact Information for Business Card

0438517264
dale@tbmweldingandfabrication.com.au
www.tbmweldingandfabrication.com.au

Colors
33a6d7
0255a3

Requirements
Must have
• Dale Hutchins
my phone number 0438517264
my logo
Preferably a black card desgn
Nice to have
• List of what i do,
Sheds and carports
Ute trays
Stockyards
Trailers
Farm equipment
Stockcrates
Gateways and Entrances
Breakdowns
Maintenance
And lots more!

```html
<!DOCTYPE html>
<html lang="en">
<head>
<meta charset="utf-8">
<title>Tbm Welding &amp; Fabrication — Business Card</title>
<link rel="stylesheet" href="https://fonts.googleapis.com/css2?family=Montserrat:wght@400;500;700;800&display=swap">
<style>
  :root {
    --backdrop: #e8e4dd;
    --card-black: #000000;
    --card-white: #ffffff;
    --brand-blue: #174a8f;
    --steel-grey: #4d5866;
    --text-white: #ffffff;
    --font-main: "Montserrat", Arial, sans-serif;
  }
  * { margin: 0; padding: 0; box-sizing: border-box; }
  html, body {
    width: 1200px; height: 800px; overflow: hidden;
    background: var(--backdrop);
    font-family: var(--font-main);
  }
  .canvas { position: relative; width: 1200px; height: 800px; }

  .card {
    position: absolute; left: 341px; width: 589px; height: 336px;
    background: var(--card-black); overflow: hidden;
    box-shadow: 0 4px 14px rgba(0,0,0,0.25);
  }
  .card--front { top: 35px; }
  .card--back { top: 420px; }

  /* Front */
  .front-top {
    position: absolute; left: 0; top: 0; width: 100%; height: 206px;
    background: var(--card-white);
  }
  .owner-name {
    position: absolute; right: 14px; top: 36px;
    font-size: 29px; font-weight: 800; color: var(--brand-blue);
    letter-spacing: -0.5px; line-height: 1;
  }
  .brand-name {
    position: absolute; left: 0; right: 0; top: 60px;
    text-align: center;
    font-size: 150px; font-weight: 800; color: var(--brand-blue);
    line-height: 1; letter-spacing: 2px;
  }
  .tagline {
    position: absolute; left: 0; right: 0; top: 208px;
    text-align: center;
    font-size: 33px; font-weight: 700; color: var(--steel-grey);
    letter-spacing: -1px; line-height: 1;
  }
  .phone {
    position: absolute; left: 0; right: 0; top: 248px;
    text-align: center; padding-right: 16px;
    font-size: 40px; font-weight: 800; color: var(--steel-grey);
    line-height: 1;
  }
  .web-links {
    position: absolute; left: 98px; top: 288px;
    font-size: 13.5px; font-weight: 500; color: var(--text-white);
    line-height: 17px;
  }
  .web-links .site { padding-left: 12px; display: block; }
  .web-links .email { display: block; }

  /* Back */
  .services-heading {
    position: absolute; left: 48px; top: 5px;
    writing-mode: vertical-rl;
    font-size: 25px; font-weight: 800; color: var(--text-white);
    line-height: 1;
  }
  .services-rule {
    position: absolute; left: 95px; top: 0; width: 5px; height: 179px;
    background: var(--steel-grey);
  }
  .services-list {
    position: absolute; left: 123px; top: 0; list-style: none;
    font-size: 18px; font-weight: 500; color: var(--text-white);
    line-height: 23.3px;
  }
  .services-list b { font-weight: 800; }
  .services-more {
    position: absolute; left: 121px; top: 212px;
    font-size: 50px; font-weight: 800; color: var(--steel-grey);
    line-height: 41px; text-transform: uppercase;
  }
  .back-brand {
    position: absolute; left: 424px; top: 260px;
    font-size: 56px; font-weight: 800; color: var(--steel-grey);
    line-height: 1;
  }
</style>
</head>
<body>
<main class="canvas">
  <section class="card card--front" aria-label="Card front">
    <div class="front-top"></div>
    <p class="owner-name">DALE HUTCHINS</p>
    <p class="brand-name">TBM</p>
    <p class="tagline">WELDING &amp; FABRICATION</p>
    <p class="phone">0438517264</p>
    <p class="web-links">
      <span class="site">www.tbmweldingandfabrication.com.au</span>
      <span class="email">dale@tbmweldingandfabrication.com.au</span>
    </p>
  </section>

  <section class="card card--back" aria-label="Card back">
    <h2 class="services-heading">MY Services</h2>
    <div class="services-rule"></div>
    <ul class="services-list">
      <li>Sheds and carports</li>
      <li>Ute trays</li>
      <li>Stock<b>YARDS</b></li>
      <li>Trailers</li>
      <li><b>FARM EQUIPMENT</b></li>
      <li>Stockcrates</li>
      <li><b>Gateways</b> and Entrances</li>
      <li><b>BREAK</b>downs</li>
      <li>Maintenance</li>
    </ul>
    <p class="services-more">And<br>lots<br>more</p>
    <p class="back-brand">TBM</p>
  </section>
</main>
</body>
</html>
```